Design of a Flyer for my Lending team, depicts me at the top - leading the team

Need to design a Team flyer to be given to business partners and customers. The Velasko Team - Home Loan group is a team within Brightwell Home Loans. The brightwell home loans brand could be small than my brand. The purpose is to brand myself and my team in the marketplace while depicting a transaparent mortgage process.
See sample flyers. The flyer should be color and web and social media friendly as i will be posting on social media and HTML emails

Target Market(s)

Business to business and business to client

Industry/Entity Type

Mortgage Lender

Font styles to use
Serif
Sans Serif

Colors

Designer to choose colors to be used in the design.

Requirements
Must have
• My team Logo powered by Brightwell HOme loans
Nice to have
• Every team member picture and bio

```html
<!DOCTYPE html>
<html lang="en">
<head>
<meta charset="utf-8">
<title>The Velasko Team – Team Flyer</title>
<link href="https://fonts.googleapis.com/css2?family=Archivo:wght@700;800&family=Arimo:wght@400;700&display=swap" rel="stylesheet">
<style>
  :root{
    --paper:#ffffff;
    --brand-blue:#2f5a8e;
    --logo-blue:#1f5fa8;
    --ink:#2a2a2a;
    --muted:#555555;
    --rule:#2b2b2b;
    --footer:#3a3a3a;
    --footer-ink:#eeeeee;
  }
  *{margin:0;padding:0;box-sizing:border-box}
  html,body{width:888px;height:1200px;overflow:hidden;background:var(--paper)}
  body{font-family:"Arimo",Arial,sans-serif;color:var(--ink);position:relative}

  .header{position:absolute;left:0;top:0;width:888px;height:124px}
  .team-mark{position:absolute;left:214px;top:34px;display:flex;align-items:center;gap:10px}
  .team-mark .square{width:26px;height:26px;background:var(--logo-blue)}
  .team-mark .name{color:var(--logo-blue);font-weight:700;text-align:center;line-height:1}
  .team-mark .name .l1{display:block;font-size:23px;letter-spacing:.2px}
  .team-mark .name .l2{display:block;font-size:11px;letter-spacing:3.5px;margin-top:5px}
  .lender-mark{position:absolute;left:478px;top:50px;display:flex;align-items:center;gap:9px}
  .lender-mark .square{width:22px;height:22px;background:var(--brand-blue)}
  .lender-mark .name{color:var(--brand-blue);font-weight:700;font-size:15px;letter-spacing:1.5px;line-height:1.1}

  .hero{position:absolute;left:0;top:124px;width:888px;height:298px;
    background:linear-gradient(180deg,#e4e6e8 0%,#cdd0d3 40%,#8a8e92 75%,#3a3b3d 100%)}
  .hero-title{position:absolute;left:0;width:888px;top:366px;text-align:center;padding-left:36px;
    font-family:"Archivo",Arial,sans-serif;font-weight:800;font-size:37px;color:#fff;letter-spacing:.3px;line-height:44px}
  .hero-rule{position:absolute;left:0;top:422px;width:888px;height:5px;background:var(--rule)}

  .member{position:absolute;left:0;width:888px}
  .member .portrait{position:absolute;left:39px;top:0;width:102px;
    background:linear-gradient(180deg,#d9dadc 0%,#9a9ea3 60%,#2d2f33 100%);border:1px solid #bbb}
  .member .name{position:absolute;left:155px;font-family:"Archivo",Arial,sans-serif;font-weight:700;font-size:25px;color:#1d1d1d;line-height:26px}
  .member .role{position:absolute;left:156px;font-size:10px;line-height:12px;color:var(--muted)}
  .member .contact{position:absolute;left:141px;width:314px;background:var(--brand-blue);color:#fff;
    font-size:13.5px;line-height:1.3;padding:6px 12px 5px 15px;box-shadow:0 6px 6px -3px rgba(0,0,0,.25)}
  .member .contact.two-line{padding-top:22px}
  .member .bio{position:absolute;left:471px;width:354px;font-size:12.6px;line-height:1.38;color:#333;text-align:justify}

  .footer{position:absolute;left:0;top:1104px;width:888px;height:96px;background:var(--footer);
    color:var(--footer-ink);font-size:10.3px;line-height:1.35;text-align:center;padding:10px 28px}
</style>
</head>
<body>
  <header class="header">
    <div class="team-mark">
      <span class="square"></span>
      <span class="name"><span class="l1">THE VELASKO TEAM</span><span class="l2">HOME LOAN GROUP</span></span>
    </div>
    <div class="lender-mark">
      <span class="square"></span>
      <span class="name">BRIGHTWELL<br>HOME LOANS</span>
    </div>
  </header>

  <section class="hero" role="img" aria-label="Team photo: three colleagues in an office reviewing work at a desk"></section>
  <h1 class="hero-title">THE VELASKO TEAM</h1>
  <div class="hero-rule"></div>

  <article class="member" style="top:450px">
    <div class="portrait" style="height:127px" role="img" aria-label="Portrait of Adrian Velasko"></div>
    <h2 class="name" style="top:0">Adrian Velasko</h2>
    <p class="role" style="top:29px">Producing Branch Manager</p>
    <p class="contact" style="top:52px;height:77px;padding-top:8px">Brightwell Home Loans, Inc – NMLS 40001<br>Adrian.Velasko@brightwellhomeloans.com<br>(407) 555-0150 Office (855) 555-0199 Fax</p>
    <p class="bio" style="top:3px">I have over 15 years of experience in Mortgage Planning. I rank in the top 1% of loan originators in the country. I pride myself on making the home buying process as smooth as possible. I will guide you through the mortgage process and look forward to helping you with your transaction. My team has been awarded with the Circle of Excellence award and CEO Club for being in the top 5 teams in the country having helped over 700+ families achieve the dream of home ownership between the years 2016 and 2017 and counting.</p>
  </article>

  <article class="member" style="top:628px">
    <div class="portrait" style="height:127px" role="img" aria-label="Portrait of Helena Brandt"></div>
    <h2 class="name" style="top:2px">Helena Brandt</h2>
    <p class="role" style="top:30px">Closing Coordinator/Team Leader – NMLS 2000117</p>
    <p class="contact two-line" style="top:55px;height:72px;padding-top:18px">Helena.Brandt@brightwellhomeloans.com<br>(631) 555-0117 Direct/Text</p>
    <p class="bio" style="top:27px">I guide our clients with any conditions or stipulations set by underwriting post loan conditional approval. I make sure all the transaction deadlines are met and help with preparing the loan for closing. I have over 20 years of experience with mortgage operations. I am committed to making sure all transactions close on time.</p>
  </article>

  <article class="member" style="top:786px">
    <div class="portrait" style="height:130px" role="img" aria-label="Portrait of Mateo Ruiz"></div>
    <h2 class="name" style="top:4px">Mateo Ruiz</h2>
    <p class="role" style="top:32px">Loan Processor – NMLS ID: 2000245</p>
    <p class="contact two-line" style="top:52px;height:78px">Mateo.Ruiz@brightwellhomeloans.com<br>(407) 555-0194 Direct/Text</p>
    <p class="bio" style="top:46px">I verify loan documents including income, credit, appraisal and title insurance, preparing the loan application for submittal to underwriting. I review file documentation and make sure all items needed to ensure a smooth mortgage transaction are requested.</p>
  </article>

  <article class="member" style="top:944px">
    <div class="portrait" style="height:129px" role="img" aria-label="Portrait of Daniel Serrano"></div>
    <h2 class="name" style="top:0">Daniel Serrano</h2>
    <p class="role" style="top:28px">Loan Partner I – NMLS ID 2000388</p>
    <p class="contact" style="top:50px;height:79px;padding-top:4px">Daniel.Serrano@brightwellhomeloans.com<br>(ants i and real estate agents informed<br>during the application process.<br>(407) 555-0172 Direct/Text</p>
    <p class="bio" style="top:55px">I am able to help customers with pre-qualifications and pre-approvals and keep the applicants i and real estate agents informed during the application process.</p>
  </article>

  <footer class="footer">Brightwell Home Loans, Inc. and any above mentioned companies are not affiliated. Brightwell Home Loans, Inc., 800 Harbor Way, Lakeview, TX 75000 NMLS ID #40000 (http://www.lenderregistry-example.org/company/40000). 1-800-555-0142. Copyright © 2018. All Rights Reserved. This is not an offer to enter into an agreement. Not all customers will qualify. Information, rates, and programs are subject to change without prior notice. All products are subject to credit and property approval. Not all products are available in all states or for all dollar amounts. If you are refinancing your existing loan, your total finance charges may be higher over the life of the loan. Other restrictions and limitations apply.</footer>
</body>
</html>
```